Brand Business Card for Hotel Cloud Management System

Hello designers,
we are looking for a new brand business card for our product Stayvora. Our brand Stayvora is a hotel management system for small hotels, B&B, guesthouses etc. and just recently we are expanding our offer to other European markets. Therefore we need a business card that will communicate not only to the end-users (hoteliers) but also to potential business partners/ We would like the brand business card to be professional looking, but not too serius, modern, elegant, clean, Our brand color is orange, dark grey and it would be nice to see both combined.

Please visit our website www.stayvora.eu to get more impression on what our brand stayvora stands for.

Please find attached stayvora logo.

Target Market(s)

small hotels, hoteliers, B&B owners, potential business partners

Industry/Entity Type

Software Service

Contact Information for Business Card

Stayvora
- hotel software solutions - web booking engine - multi channel manager
www.stayvora.eu
T: +38614738265
E: info@stayvora.net

Font styles to use
Serif
Sans Serif

Colors
f37122
aaaaaa
606060
f6f6f6

Requirements
Must have
• Logo of the brand
• the layout of the business card should be in connection with the look and feel of the website stayvora.eu and logo stayvora;

```html
<!DOCTYPE html>
<html lang="en">
<head>
<meta charset="UTF-8">
<title>Stayvora – Business Card</title>
<link href="https://fonts.googleapis.com/css2?family=Open+Sans:wght@400;600;700;800&display=swap" rel="stylesheet">
<style>
  :root {
    --orange: #f37122;
    --ink: #111111;
    --card-black: #1b1b1b;
    --emboss: #2f2f2f;
    --grey-mid: #606060;
    --grey-light: #aaaaaa;
    --paper: #ffffff;
    --stage: #dcdcdc;
  }
  * { box-sizing: border-box; margin: 0; padding: 0; }
  html, body {
    width: 1200px; height: 900px; overflow: hidden;
    background: var(--stage);
    font-family: "Open Sans", Arial, sans-serif;
  }
  .stage {
    width: 1200px; height: 900px;
    display: flex; align-items: center; justify-content: center; gap: 44px;
  }
  .card {
    width: 540px; height: 350px;
    border-radius: 30px;
    position: relative;
    overflow: hidden;
  }

  /* Front */
  .card--front { background: var(--paper); }
  .brand {
    position: absolute; top: 52px; left: 0; right: 0;
    display: flex; flex-direction: column; align-items: center;
  }
  .brand__row { display: flex; align-items: center; gap: 10px; }
  .brand__mark {
    width: 26px; height: 26px; border-radius: 5px; background: var(--orange);
  }
  .brand__name {
    font-weight: 800; font-size: 50px; line-height: 1; letter-spacing: -1.5px;
    color: var(--ink);
  }
  .brand__tagline {
    margin-top: 4px; font-size: 15px; color: var(--ink); letter-spacing: 0.2px;
  }
  .contacts {
    position: absolute; left: 26px; right: 26px; top: 162px;
    display: flex; justify-content: space-between;
  }
  .contact { display: flex; flex-direction: column; align-items: center; gap: 12px; }
  .contact__icon {
    width: 50px; height: 50px; border-radius: 12px; background: var(--ink);
    display: flex; align-items: center; justify-content: center;
  }
  .contact__pill {
    width: 156px; height: 44px; border-radius: 14px; background: var(--orange);
    color: var(--ink); font-size: 14px; font-weight: 600; letter-spacing: -0.3px;
    display: flex; align-items: center; justify-content: center;
  }
  .services {
    position: absolute; left: 0; right: 0; bottom: 34px;
    text-align: center; font-size: 13px; color: var(--ink);
    letter-spacing: -0.4px; text-transform: uppercase;
  }
  .services__sep { margin: 0 8px; }

  /* Back */
  .card--back { background: var(--card-black); }
  .back-brand {
    position: absolute; inset: 0;
    display: flex; flex-direction: column; align-items: center; justify-content: center;
  }
  .back-brand__row { display: flex; align-items: center; gap: 12px; }
  .back-brand__mark { width: 30px; height: 30px; border-radius: 6px; background: var(--orange); }
  .back-brand__name {
    font-weight: 800; font-size: 62px; line-height: 1; letter-spacing: -2px; color: var(--emboss);
  }
  .back-brand__tagline {
    margin-top: 6px; font-size: 17px; color: var(--grey-mid);
  }
  .back-brand__url {
    margin-top: 22px; font-size: 15px; letter-spacing: 7px; color: var(--orange);
  }
</style>
</head>
<body>
<main class="stage">
  <section class="card card--front" aria-label="Card front">
    <div class="brand">
      <div class="brand__row">
        <span class="brand__name">Stayvora</span>
        <span class="brand__mark"></span>
      </div>
      <span class="brand__tagline">hotel pms service</span>
    </div>

    <div class="contacts">
      <div class="contact">
        <span class="contact__icon">
          <svg width="28" height="20" viewBox="0 0 28 20" aria-hidden="true">
            <rect x="1" y="1" width="26" height="18" fill="var(--orange)"/>
            <path d="M1 1 L14 12 L27 1" fill="none" stroke="var(--ink)" stroke-width="1.6"/>
            <path d="M1 19 L11 9 M27 19 L17 9" fill="none" stroke="var(--ink)" stroke-width="1.2"/>
          </svg>
        </span>
        <span class="contact__pill">info@stayvora.net</span>
      </div>
      <div class="contact">
        <span class="contact__icon">
          <svg width="30" height="26" viewBox="0 0 30 26" aria-hidden="true">
            <path d="M2 9 C2 2 28 2 28 9 L22 10 L21 6 L9 6 L8 10 Z" fill="var(--orange)"/>
            <path d="M8 11 L22 11 L26 24 L4 24 Z" fill="var(--orange)"/>
            <circle cx="15" cy="17" r="4" fill="var(--ink)"/>
            <circle cx="15" cy="17" r="1.6" fill="var(--orange)"/>
          </svg>
        </span>
        <span class="contact__pill">+38614738265</span>
      </div>
      <div class="contact">
        <span class="contact__icon">
          <svg width="28" height="28" viewBox="0 0 28 28" aria-hidden="true" fill="none" stroke="var(--orange)" stroke-width="1.8">
            <circle cx="14" cy="14" r="12"/>
            <ellipse cx="14" cy="14" rx="5.5" ry="12"/>
            <line x1="2" y1="14" x2="26" y2="14"/>
            <path d="M4 8 H24 M4 20 H24"/>
          </svg>
        </span>
        <span class="contact__pill">www.stayvora.eu</span>
      </div>
    </div>

    <p class="services">Hotel software solutions<span class="services__sep">/</span>Web booking engine<span class="services__sep">/</span>Multi channel manager</p>
  </section>

  <section class="card card--back" aria-label="Card back">
    <div class="back-brand">
      <div class="back-brand__row">
        <span class="back-brand__name">Stayvora</span>
        <span class="back-brand__mark"></span>
      </div>
      <span class="back-brand__tagline">hotel pms service</span>
      <span class="back-brand__url">www.stayvora.eu</span>
    </div>
  </section>
</main>
</body>
</html>
```